Power Point CI

Creat a Slide Master which we can use and also add new slides with bullets, or other graphic design which we can fill. Power Point Master Format - also amend the graphics on the PPT - especially the project roadmap or profile page. have a look on our website www.brightlantern.io. I would also appreciate other slides which we can use and fill

Target Market(s)

companies - PE, HR Executive

Industry/Entity Type

Executive Search

Font styles to use
Serif
Other font styles liked:
• Calibri or Coast like on our website

Colors
0094D4
00A9DD
6FCCEA
C7EBF8
E9F6FB

Requirements
Must have
• needs to sleek and slim - prefer white and bright elegant Backgrounds
Nice to have
• it should somehow fit to our website and corporate CI
Should not have
• Full green CI

```html
<!DOCTYPE html>
<html lang="en">
<head>
<meta charset="utf-8">
<title>Bright Lantern – Slide Master Overview</title>
<link href="https://fonts.googleapis.com/css2?family=Fira+Sans:wght@300;400;500;600;700&family=Montserrat:wght@400;500;700;800&display=swap" rel="stylesheet">
<style>
:root{
  --bg:#d9dadc;
  --teal-deep:#0b4656;
  --teal:#0d5a6c;
  --teal-mid:#2f8594;
  --teal-soft:#5bb4c0;
  --teal-pale:#93d2d9;
  --row-tint:#e6eef0;
  --ink:#4d5559;
  --ink-soft:#7a8387;
  --white:#ffffff;
}
*{margin:0;padding:0;box-sizing:border-box}
html,body{width:1200px;height:1154px;overflow:hidden;background:var(--bg)}
body{position:relative;font-family:"Fira Sans",Arial,sans-serif;color:var(--ink)}
.slide{position:absolute;width:367px;height:206px;background:var(--white);overflow:hidden;box-shadow:0 1px 3px rgba(0,0,0,.12)}
.abs{position:absolute}
.c1{left:38px}.c2{left:416px}.c3{left:795px}
.r1{top:36px}.r2{top:255px}.r3{top:473px}.r4{top:692px}.r5{top:911px}

/* footer */
.footer-brand{position:absolute;left:10px;top:187px;font-size:4.6px;letter-spacing:.6px;color:var(--teal-soft);font-weight:400}
.footer-rule{position:absolute;left:47px;right:17px;top:190px;height:.5px;background:var(--teal)}
.footer-page{position:absolute;right:6px;top:187px;font-size:4.6px;font-weight:700;color:var(--teal-deep)}

/* type */
.title{position:absolute;font-weight:600;color:var(--teal);white-space:nowrap}
.title-bar{position:absolute;height:3px;background:var(--teal);border-radius:0 2px 2px 0}
.body{position:absolute;font-size:4.2px;line-height:1.45;color:var(--ink)}
.body p{margin-bottom:3.2px}
.hl{color:var(--teal);font-weight:500}

/* cover & closing */
.cover{background:linear-gradient(135deg,#1a6f80 0%,#0d5465 45%,#073746 100%)}
.brand-large{position:absolute;left:130px;top:106px;font-size:20px;font-weight:300;letter-spacing:3px;color:var(--white)}
.brand-dot{position:absolute;left:116px;top:112px;width:8px;height:8px;border-radius:50%;background:var(--white)}
.cover-rule{position:absolute;top:179px;height:.6px;background:rgba(255,255,255,.8)}
.cities{position:absolute;left:123px;top:175px;font-size:7px;color:var(--white);letter-spacing:.2px}
.thanks{position:absolute;left:114px;top:88px;font-size:33px;font-weight:600;color:var(--white)}

/* contents */
.toc-line{position:absolute;background:var(--ink-soft)}
.toc-item{position:absolute;left:224px;width:120px}
.toc-item h4{font-size:6.6px;font-weight:600;color:var(--teal)}
.toc-item p{font-size:3.6px;line-height:1.35;color:var(--ink);margin-top:1.5px}
.toc-item.marked p{background:#3b4648;color:#cfd6d8;padding:.5px 1px}

/* profile */
.frame-block{position:absolute;background:var(--teal)}
.portrait{position:absolute;background:linear-gradient(160deg,#6e6e6e 0%,#2c2c2c 60%,#1a1a1a 100%)}
.person-name{position:absolute;font-size:16px;font-weight:600;color:var(--teal)}

/* bullet lists */
.bullets{position:absolute;list-style:none;font-size:4.8px;line-height:1.4;color:var(--ink)}
.bullets li{position:relative;padding-left:7px;margin-bottom:5px}
.bullets li::before{content:"";position:absolute;left:0;top:1.8px;width:1.8px;height:1.8px;background:var(--teal)}

/* values */
.value{position:absolute;width:147px}
.value h3{font-size:8px;font-weight:600;color:var(--teal);padding-bottom:2px;border-bottom:.6px solid var(--teal-deep);position:relative}
.value h3::after{content:"";position:absolute;left:0;bottom:-1.6px;width:54px;height:2.4px;background:var(--teal)}
.value p{font-size:4.3px;line-height:1.55;margin-top:7px;text-align:justify}

/* tables */
.ref-table{position:absolute;width:148px;border:.6px solid var(--teal);border-collapse:collapse;font-size:4.4px;color:#333}
.ref-table th{background:var(--teal);color:var(--white);font-size:10px;font-weight:500;height:21px;text-align:left;padding-left:9px;letter-spacing:.2px}
.ref-table td{height:15.6px;padding-left:3px}
.ref-table tr:nth-child(even) td{background:var(--row-tint)}

/* target universe */
.tu-block{position:absolute;width:80px}
.tu-block h4{font-size:5px;font-weight:500;color:var(--teal)}
.tu-block.soft h4{color:var(--teal-mid)}
.tu-block p{font-size:3.7px;line-height:1.35;color:var(--ink-soft);margin:2px 0 3px 6px}

/* candidate profile */
.tile{position:absolute;width:45px;height:44px;font-size:3.6px;color:var(--white);text-align:center;padding-top:36px}
.tile.deep{background:var(--teal)}.tile.mid{background:var(--teal-mid)}.tile.soft{background:var(--teal-soft)}.tile.pale{background:var(--teal-pale)}
.tile::before{content:"";position:absolute;left:18px;top:7px;width:9px;height:24px;border-radius:4px;background:rgba(255,255,255,.9)}

/* caps slides */
.caps{position:absolute;font-family:"Montserrat",Arial,sans-serif;color:var(--teal);line-height:1.1}
.caps b{font-weight:800}
.plain-list{position:absolute;list-style:none;font-family:"Montserrat",Arial,sans-serif;font-size:8.4px;color:#666;line-height:1}
.plain-list li{margin-bottom:6.1px;position:relative;padding-left:7px}
.plain-list li::before{content:"";position:absolute;left:0;top:3px;width:2.4px;height:2.4px;background:#666}
.tick-list li{padding-left:15px}
.tick-list li::before{width:5px;height:2.6px;border-left:1px solid #666;border-bottom:1px solid #666;background:none;transform:rotate(-45deg);top:1.5px}
.lorem-list{position:absolute;list-style:none;font-size:4.3px;line-height:1.3;color:#555;width:155px}
.lorem-list li{position:relative;padding-left:6px;margin-bottom:5px}
.lorem-list li::before{content:"";position:absolute;left:0;top:1.2px;width:2px;height:2px;border-radius:50%;background:var(--teal)}
.lorem-list b{color:var(--teal);font-weight:600}

/* digital tool */
.screen{position:absolute;background:linear-gradient(180deg,#f4f6f7,#e8ecee);border:.6px solid #d4d9dc;box-shadow:0 1px 3px rgba(0,0,0,.15)}
.feature{position:absolute;left:220px;width:120px;font-size:5.2px;line-height:1.35;color:var(--ink)}
.feature-icon{position:absolute;left:204px;width:10px;height:10px}

/* active intelligence */
.photo{position:absolute;background:linear-gradient(180deg,#e9eff2 0%,#b9c7cf 45%,#6d7f8b 75%,#c5ccd1 100%)}
.teal-panel{position:absolute;background:linear-gradient(160deg,#3a95a0,#1f7583)}
.panel-text{position:absolute;font-size:4.7px;line-height:1.3;color:var(--white);text-align:justify}
</style>
</head>
<body>

<!-- 01 cover -->
<section class="slide c1 r1 cover">
  <span class="brand-dot"></span>
  <div class="brand-large">BRIGHT LANTERN</div>
  <div class="cover-rule" style="left:0;width:118px"></div>
  <div class="cities">Hamburg / Wien / Berlin / München</div>
  <div class="cover-rule" style="left:251px;right:0"></div>
</section>

<!-- 02 contents -->
<section class="slide c2 r1">
  <div class="title" style="left:126px;top:93px;font-size:17px">Contents</div>
  <div class="toc-line" style="left:214px;top:46px;width:.6px;height:111px"></div>
  <div class="toc-line" style="left:206px;top:103px;width:8px;height:.6px"></div>
  <div class="toc-line" style="left:214px;top:46px;width:7px;height:.6px"></div>
  <div class="toc-line" style="left:214px;top:81px;width:7px;height:.6px"></div>
  <div class="toc-line" style="left:214px;top:123px;width:7px;height:.6px"></div>
  <div class="toc-line" style="left:214px;top:157px;width:7px;height:.6px"></div>
  <div class="toc-item" style="top:42px"><h4>Lorem ipsum</h4><p>Lorem ipsum dolor sit amet, consectetuer adipiscing elit, sed diam nonummy nibh euismod tincid</p></div>
  <div class="toc-item" style="top:77px"><h4>Lorem ipsum</h4><p>Lorem ipsum dolor sit amet, consectetuer adipiscing elit, sed diam nonummy nibh euismod tincid</p></div>
  <div class="toc-item marked" style="top:119px"><h4>Lorem ipsum</h4><p>Lorem ipsum dolor sit amet, consectetuer adipiscing elit, sed diam nonummy nibh euismod tincid</p></div>
  <div class="toc-item" style="top:153px"><h4>Lorem ipsum</h4><p>Lorem ipsum dolor sit amet, consectetuer adipiscing elit, sed diam nonummy nibh euismod tincid</p></div>
  <div class="footer-brand">BRIGHT LANTERN</div><div class="footer-rule"></div><div class="footer-page">02</div>
</section>

<!-- 03 profile -->
<section class="slide c3 r1">
  <div class="frame-block" style="left:24px;top:32px;width:61px;height:82px"></div>
  <div class="portrait" role="img" aria-label="Black and white portrait photo of Dr. Helena Marquardt-Voss" style="left:38px;top:45px;width:82px;height:121px"></div>
  <div class="person-name" style="left:133px;top:53px">Dr. Helena Marquardt-Voss</div>
  <div class="body" style="left:133px;top:82px;width:210px">
    <p>Helena knows what modern management is all about, and that from many points of view – she has not only successfully appointed many to leadership positions, but she has held those positions herself several times.</p>
    <p>As a graduate of medicine of the Lindenberg University Hospital, she first started working for Brantley &amp; Co, where she led the Brantley Hospital Academy. At Harwood Partners, she was responsible for the German healthcare sector. She was a founder and CEO of a healthcare tech start-up, which she successfully sold to an investor. And she was the CHRO of another startup that scaled very fast. To share this comprehensive experience with many companies, she founded Bright Lantern Executive Search in 2021.</p>
    <p>Helena lives in Hamburg with her family.</p>
  </div>
  <div class="footer-brand">BRIGHT LANTERN</div><div class="footer-rule"></div><div class="footer-page">03</div>
</section>

<!-- 04 profile -->
<section class="slide c1 r2">
  <div class="frame-block" style="left:25px;top:32px;width:61px;height:83px"></div>
  <div class="portrait" role="img" aria-label="Black and white portrait photo of Clara Brenner" style="left:38px;top:46px;width:81px;height:120px"></div>
  <div class="person-name" style="left:132px;top:52px">Clara Brenner</div>
  <div class="body" style="left:132px;top:78px;width:210px">
    <p>Clara started her career as a Global Product Manager at Keller Tools in Schaan/Liechtenstein before she spent 3 years in London as the European Sales Manager for Skyline Airways.</p>
    <p>She then accepted an offer from Harwood Partners (HP) where she learned the skills of research.</p>
    <p>When her partner was transferred to Bogota in Colombia, she became self-employed (working primarily for HP), and now, back in Vienna, she founded Bright Lantern Executive Search together with Helena.</p>
    <p>Clara studied International Business Administration at the Danube School of Economics and Business and also graduated from the Meridian programme. She is mother of 2 children.</p>
  </div>
  <div class="footer-brand">BRIGHT LANTERN</div><div class="footer-rule"></div><div class="footer-page">04</div>
</section>

<!-- 05 who we are -->
<section class="slide c2 r2">
  <div class="title" style="left:31px;top:25px;font-size:16.5px">Who We Are and How We Work</div>
  <ul class="bullets" style="left:38px;top:64px;width:125px">
    <li><span class="hl">Longstanding experience</span> with a passion for placing (C-Level) Executives in Healthcare and other industries</li>
    <li>In-depth expertise strong networks in health care and , covering all <span class="hl">relevant sub-sectors</span> (HC Services, PE Healthcare Rollups, Elderly Care Chains, Physiotherapy, Digital Health, Medical Technology, Healthcare IT), including relevant expertise regarding the regulatory environment in Germany</li>
    <li>Expertise beyond placement and HR topics, allowing for eye-level discussion around your business</li>
  </ul>
  <ul class="bullets" style="left:193px;top:64px;width:130px">
    <li><span class="hl">Creative approaches</span> to finding - and convincing – candidates</li>
    <li><span class="hl">Structured</span> and lean <span class="hl">digital search processes</span>, high transparency, comprehensive candidate evaluation</li>
    <li><span class="hl">Referencing</span> of candidates as part of the search process; psychometrics on demand</li>
    <li>Onboarding support to ensure a good start for the candidate</li>
    <li>We work with you <span class="hl">personally</span> and act as an <span class="hl">ambassador</span> for our clients in the market</li>
  </ul>
  <div class="footer-brand">BRIGHT LANTERN</div><div class="footer-rule"></div><div class="footer-page">05</div>
</section>

<!-- 06 values -->
<section class="slide c3 r2">
  <div class="title" style="left:18px;top:9px;font-size:19.5px">Our Values</div>
  <div class="title-bar" style="left:18px;top:35px;width:75px;height:2.4px"></div>
  <div class="value" style="left:28px;top:50px"><h3>HONEST</h3><p>We only work with clients who can benefit from our expertise. We are not interested in status symbols, only in achieving results in a way that is transparent and beneficial for everyone.</p></div>
  <div class="value" style="left:197px;top:50px"><h3>PRAGMATIC</h3><p>We work fast. But we don’t start until we have a clear goal: We begin by asking “How will you know the appointment was successful, 3 years from now?” This thought drives our process – streamlined, digital, and constantly in communication with you, from the briefing to your new staff member’s first day.</p></div>
  <div class="value" style="left:28px;top:120px"><h3>PERSONAL</h3><p>We put all of our resources into finding you the top talents you are looking for – and we get involved ourselves. We have excellent networks, and we are always hot on the heels of fresh talent. That is how we find the people that you need right now. And we help them realise that your company is the right place for them.</p></div>
  <div class="value" style="left:197px;top:120px"><h3>DIVERSE</h3><p>We know where the obstacles lie, and we know where things get tough – we have worked through them ourselves, as employees, as managers, as founders, and as mothers. That’s how we know how diversity really works, and how diversity can best benefit your company.</p></div>
  <div class="footer-brand">BRIGHT LANTERN</div><div class="footer-rule"></div><div class="footer-page">06</div>
</section>

<!-- 07 references -->
<section class="slide c1 r3">
  <div class="title" style="left:29px;top:22px;font-size:13.5px">Relevant reference assignments (excerpt)</div>
  <div class="title-bar" style="left:29px;top:47px;width:118px"></div>
  <table class="ref-table" style="left:29px;top:66px">
    <tr><th colspan="2">POSITION TO BE DEFINED</th></tr>
    <tr><td>Explanation</td><td>Investor/Owner</td></tr>
    <tr><td>Explanation</td><td>Investor/Owner</td></tr>
    <tr><td>Explanation</td><td>Investor/Owner</td></tr>
    <tr><td>Explanation</td><td>Investor/Owner</td></tr>
    <tr><td>Explanation</td><td>Investor/Owner</td></tr>
  </table>
  <table class="ref-table" style="left:190px;top:66px">
    <tr><th colspan="2">POSITION TO BE DEFINED</th></tr>
    <tr><td>Explanation</td><td>Investor/Owner</td></tr>
    <tr><td>Explanation</td><td>Investor/Owner</td></tr>
    <tr><td>Explanation</td><td>Investor/Owner</td></tr>
    <tr><td>Explanation</td><td>Investor/Owner</td></tr>
    <tr><td>Explanation</td><td>Investor/Owner</td></tr>
  </table>
  <div class="footer-brand">BRIGHT LANTERN</div><div class="footer-rule"></div><div class="footer-page">07</div>
</section>

<!-- 08 target universe -->
<section class="slide c2 r3">
  <div class="title" style="left:16px;top:14px;font-size:17px">Target Universe</div>
  <div class="tu-block" style="left:22px;top:54px"><h4>1. Direct competition</h4><p>Lorem ipsum dolor sit amet, consectetuer adipiscing elit, sed diam nonummy nibh euismod tincidunt.</p><p>ut laoreet dolore magna aliquam erat volutpat. Ut wisi enim ad minim veniam, quis nostrud exerci tation</p></div>
  <div class="tu-block soft" style="left:119px;top:54px"><h4>2. To be defined</h4><p>Lorem ipsum dolor sit amet, consectetuer adipiscing elit.</p><p>sed diam nonummy nibh euismod tincidunt ut laoreet dolore magna aliquam erat volutpat. Ut wisi enim ad minim veniam, quis nostrud exerci</p></div>
  <div class="tu-block soft" style="left:22px;top:110px"><h4>3. To be defined</h4><p>Lorem ipsum dolor sit amet, consectetuer adipiscing elit, sed diam nonummy nibh euismod tincidunt.</p><p>ut laoreet dolore magna aliquam erat volutpat. Ut wisi enim ad minim veniam, quis nostrud exerci tation</p></div>
  <div class="tu-block soft" style="left:119px;top:110px"><h4>4. To be defined</h4><p>Lorem ipsum dolor sit amet, consectetuer adipiscing elit.</p><p>sed diam nonummy nibh euismod tincidunt ut laoreet dolore magna aliquam erat volutpat. Ut wisi enim ad minim veniam, quis nostrud exerci</p></div>
  <svg class="abs" style="left:0;top:0" width="367" height="206" viewBox="0 0 367 206" font-family="Fira Sans, sans-serif">
    <circle cx="287" cy="94" r="20" fill="#c9e6ea"/>
    <circle cx="287" cy="52" r="23" fill="#4aa9b6"/>
    <circle cx="242" cy="93" r="23" fill="#2f8594"/>
    <circle cx="330" cy="94" r="23" fill="#93d2d9"/>
    <circle cx="287" cy="136" r="23" fill="#0b4656"/>
    <rect x="279" y="90" width="3" height="11" fill="#0d5a6c"/><rect x="284" y="84" width="3" height="17" fill="#0d5a6c"/><rect x="289" y="93" width="3" height="8" fill="#0d5a6c"/><rect x="277" y="101" width="18" height=".8" fill="#0d5a6c"/>
    <text x="297" y="50" font-size="11" font-weight="700" fill="#fff">B</text><text x="294" y="56" font-size="3.2" fill="#fff">Target 3</text>
    <text x="237" y="90" font-size="11" font-weight="700" fill="#fff">A</text><text x="235" y="96" font-size="3.2" fill="#fff">Target 2</text>
    <text x="332" y="105" font-size="11" font-weight="700" fill="#fff">C</text><text x="328" y="94" font-size="3.2" fill="#fff">Target 4</text>
    <text x="273" y="145" font-size="11" font-weight="700" fill="#fff">D</text><text x="270" y="134" font-size="3.2" fill="#fff">Target 4</text>
    <circle cx="277" cy="45" r="2" fill="#fff"/><rect x="275.5" y="48" width="3" height="8" rx="1" fill="#fff"/>
    <circle cx="242" cy="103" r="3" fill="#fff"/>
    <ellipse cx="334" cy="84" rx="4" ry="1.5" fill="#fff"/><rect x="330" y="84" width="8" height="4" fill="#fff"/>
    <path d="M294 140 l6 -6 l2 2 l-6 6 z" fill="#fff"/>
  </svg>
  <div class="body" style="left:16px;top:170px;font-size:4.8px">NOTE: targets are exepmplary and will be adapted throughout the process</div>
  <div class="footer-brand">BRIGHT LANTERN</div><div class="footer-rule"></div><div class="footer-page">08</div>
</section>

<!-- 09 candidate profile -->
<section class="slide c3 r3">
  <div class="title" style="left:16px;top:14px;font-size:17px">Candidate Profile – for discussion</div>
  <div class="title-bar" style="left:16px;top:40px;width:126px"></div>
  <div class="title" style="left:26px;top:73px;font-size:8.6px">Outline of relevant competencies</div>
  <ul class="bullets" style="left:32px;top:91px;width:140px;font-size:4.9px">
    <li style="margin-bottom:2.6px">We put all of our resources into finding</li>
    <li style="margin-bottom:2.6px">you the top talents you are</li>
    <li style="margin-bottom:2.6px">and we get involved ourselves. We have</li>
    <li style="margin-bottom:2.6px">excellent networks, and we are</li>
    <li style="margin-bottom:2.6px">always hot on the heels of fresh talent</li>
    <li style="margin-bottom:2.6px">That is how we find the</li>
    <li style="margin-bottom:2.6px">right now. And we help them realise</li>
  </ul>
  <div class="tile deep" style="left:212px;top:64px">Profile 1</div>
  <div class="tile soft" style="left:272px;top:64px">Profile 3</div>
  <div class="tile mid" style="left:212px;top:126px">Profile 2</div>
  <div class="tile pale" style="left:272px;top:126px">Profile 4</div>
  <div class="footer-brand">BRIGHT LANTERN</div><div class="footer-rule"></div><div class="footer-page">09</div>
</section>

<!-- 10 search process -->
<section class="slide c1 r4">
  <div class="title" style="left:12px;top:5px;font-size:15.5px">Search Process</div>
  <div class="title-bar" style="left:12px;top:26px;width:62px;height:2px"></div>
  <svg class="abs" style="left:0;top:0" width="367" height="206" viewBox="0 0 367 206" font-family="Fira Sans, sans-serif" text-anchor="middle">
    <line x1="55" y1="82" x2="310" y2="82" stroke="#0d5a6c" stroke-width=".6"/>
    <text x="47" y="84" font-size="4.6" fill="#0d5a6c">CW 1</text>
    <text x="316" y="84" font-size="4.6" fill="#0d5a6c" text-anchor="start">CW 12</text>
    <text x="101" y="47" font-size="4.4" font-weight="500" fill="#0d5a6c">Phase 1</text><text x="101" y="53" font-size="4.4" font-weight="500" fill="#0d5a6c">Research - Longlist</text>
    <text x="184" y="47" font-size="4.4" font-weight="500" fill="#2f8594">Phase 2</text><text x="184" y="53" font-size="4.4" font-weight="500" fill="#2f8594">Focus &amp; Interviews - Shortlist</text>
    <text x="264" y="47" font-size="4.4" font-weight="500" fill="#0d5a6c">Phase 3</text><text x="264" y="53" font-size="4.4" font-weight="500" fill="#0d5a6c">Completion</text>
    <g stroke="#0d5a6c" stroke-width=".6">
      <line x1="103" y1="107" x2="103" y2="144"/><line x1="144" y1="131" x2="144" y2="144"/><line x1="184" y1="107" x2="184" y2="144"/><line x1="225" y1="131" x2="225" y2="144"/><line x1="264" y1="107" x2="264" y2="144"/>
    </g>
    <g fill="#0d5a6c"><circle cx="103" cy="144" r="1.6"/><circle cx="144" cy="144" r="1.6"/><circle cx="184" cy="144" r="1.6"/><circle cx="225" cy="144" r="1.6" fill="#93d2d9"/><circle cx="264" cy="144" r="1.6"/></g>
    <g>
      <polygon transform="translate(103,82)" points="0,-26 22.5,-13 22.5,13 0,26 -22.5,13 -22.5,-13" fill="#fff"/>
      <polygon transform="translate(103,82)" points="0,-23 20,-11.5 20,11.5 0,23 -20,11.5 -20,-11.5" fill="#0b4656"/>
      <polygon transform="translate(184,82)" points="0,-26 22.5,-13 22.5,13 0,26 -22.5,13 -22.5,-13" fill="#fff"/>
      <polygon transform="translate(184,82)" points="0,-23 20,-11.5 20,11.5 0,23 -20,11.5 -20,-11.5" fill="#5bb4c0"/>
      <polygon transform="translate(264,82)" points="0,-26 22.5,-13 22.5,13 0,26 -22.5,13 -22.5,-13" fill="#fff"/>
      <polygon transform="translate(264,82)" points="0,-23 20,-11.5 20,11.5 0,23 -20,11.5 -20,-11.5" fill="#0b4656"/>
      <polygon transform="translate(144,106)" points="0,-26 22.5,-13 22.5,13 0,26 -22.5,13 -22.5,-13" fill="#fff"/>
      <polygon transform="translate(144,106)" points="0,-23 20,-11.5 20,11.5 0,23 -20,11.5 -20,-11.5" fill="#2f8594"/>
      <polygon transform="translate(225,106)" points="0,-26 22.5,-13 22.5,13 0,26 -22.5,13 -22.5,-13" fill="#fff"/>
      <polygon transform="translate(225,106)" points="0,-23 20,-11.5 20,11.5 0,23 -20,11.5 -20,-11.5" fill="#93d2d9"/>
    </g>
    <g fill="none" stroke="#fff" stroke-width="1.2">
      <circle cx="103" cy="75" r="5"/><circle cx="184" cy="75" r="5"/><circle cx="264" cy="75" r="5"/><circle cx="144" cy="99" r="5"/><circle cx="225" cy="99" r="5"/>
    </g>
    <g fill="#fff" font-weight="600">
      <text x="103" y="90" font-size="4.8">Kickoff</text><text x="184" y="90" font-size="4.8">Interviews</text>
      <text x="264" y="89" font-size="4">Selection final</text><text x="264" y="94" font-size="4">candidate</text>
      <text x="144" y="114" font-size="4.8">Research</text><text x="225" y="114" font-size="4.8">References</text>
    </g>
    <g font-size="4.6" font-weight="500">
      <text x="103" y="152" fill="#0d5a6c">Kickoff</text><text x="144" y="152" fill="#2f8594">Research</text><text x="184" y="152" fill="#5bb4c0">Interviews</text><text x="225" y="152" fill="#93d2d9">References</text><text x="264" y="152" fill="#0d5a6c">Selection final</text><text x="264" y="157" fill="#0d5a6c">candidate</text>
    </g>
    <g font-size="3.3" fill="#7a8387">
      <text x="103" y="157">Discuss and agree on</text><text x="103" y="161">profile, position</text><text x="103" y="165">specification and target</text><text x="103" y="169">list</text>
      <text x="144" y="157">Active and passive</text><text x="144" y="161">research, approach</text><text x="144" y="165">of potential</text><text x="144" y="169">candidates</text>
      <text x="184" y="157">Presentation</text><text x="184" y="161">of prioritised</text><text x="184" y="165">profiles, client</text><text x="184" y="169">interviews</text>
      <text x="225" y="157">Assessments</text><text x="225" y="161">(optional), taking</text><text x="225" y="165">references</text>
      <text x="264" y="162">Contract negotiation</text><text x="264" y="166">and onboarding,</text><text x="264" y="170">feedback discussion</text>
    </g>
  </svg>
  <div class="footer-brand">BRIGHT LANTERN</div><div class="footer-rule"></div><div class="footer-page">10</div>
</section>

<!-- 11 text layout -->
<section class="slide c2 r4">
  <div class="caps" style="left:21px;top:20px;font-size:14.5px">LOREM IPSUM<br><b>DOLOR SIT AMET</b></div>
  <ul class="lorem-list" style="left:21px;top:66px">
    <li><b>Lorem ipsum :</b> dolor sit amet, consectetuer adipiscing elit, nonummy nibh euismod tincidunt ut laoreet dolore magna</li>
    <li><b>Lorem ipsum :</b> dolor sit amet, consectetuer adipiscing elit, sed diam nonummy nibh euismod tincidunt ut laoreet dolore magna aliquam erat volutpat. Ut wisi enim ad min, quis nostrud exerci tation ullamcorper suscipit lobortis nisl ut</li>
    <li><b>Lorem ipsum :</b> dolor sit amet, consectetuer adipis cing elit, sed diam nonummy nibh euismod tinci dunt ut laoreet magna aliquam erat volutpat.</li>
    <li><b>Lorem ipsum :</b> dolor sit amet, consectetuer adipiscing nibh euismod tincidunt ut laoreet dolore magna</li>
    <li><b>Lorem ipsum :</b> dolor sit amet, consectetuer adipis cing elit, sed diam nonummy nibh euismod tinci dunt ut laoreet dolore.</li>
  </ul>
  <div class="caps" style="left:197px;top:28px;font-size:11.4px">WHAT'S A DOMAIN?<br>IT'S THAT NAME UP<br><b>IN THE ADDRESS BAR.</b></div>
  <ul class="plain-list" style="left:197px;top:79px">
    <li>Fits your business or products</li><li>Is easy to spell and remember</li><li>Fits your business or products</li><li>Is easy to spell and remember</li><li>Fits your business or products</li><li>Is easy to spell and remember</li><li>Fits your business or products</li>
  </ul>
  <div class="footer-brand">BRIGHT LANTERN</div><div class="footer-rule"></div><div class="footer-page">11</div>
</section>

<!-- 12 digital tool -->
<section class="slide c3 r4">
  <div class="title" style="left:10px;top:7px;font-size:15.5px">Digital Tool for Full Transparency</div>
  <div class="title-bar" style="left:10px;top:30px;width:126px"></div>
  <div class="screen" role="img" aria-label="Screenshot of the candidate tracking web tool with candidate lists" style="left:31px;top:46px;width:158px;height:123px"></div>
  <svg class="feature-icon" style="top:57px" viewBox="0 0 10 10" fill="none" stroke="#5bb4c0" stroke-width=".8"><path d="M1 9 L5 5 M9 1 L6 4 M6 1 V4 H9"/></svg>
  <div class="feature" style="top:57px">Follow the progress of the project 24/7 real-time</div>
  <svg class="feature-icon" style="top:88px" viewBox="0 0 10 10" fill="none" stroke="#5bb4c0" stroke-width=".8"><path d="M2 1V9M5 1V9M8 1V9"/><circle cx="2" cy="6" r="1" fill="#fff"/><circle cx="5" cy="3" r="1" fill="#fff"/><circle cx="8" cy="7" r="1" fill="#fff"/></svg>
  <div class="feature" style="top:88px">Prioritize and evaluate candidates and provide feedback</div>
  <svg class="feature-icon" style="top:119px" viewBox="0 0 10 10" fill="none" stroke="#5bb4c0" stroke-width=".8"><rect x=".5" y="1" width="9" height="8"/><path d="M2 7 L4 5 L6 6 L8 3"/></svg>
  <div class="feature" style="top:119px">You can view the list of target companies at any time</div>
  <svg class="feature-icon" style="top:149px" viewBox="0 0 10 10" fill="none" stroke="#5bb4c0" stroke-width=".8"><rect x="2.5" y=".5" width="5" height="9" rx="1"/></svg>
  <div class="feature" style="top:149px">Access to the relevant information on all candidates at all timesn</div>
  <div class="footer-brand">BRIGHT LANTERN</div><div class="footer-rule"></div><div class="footer-page">12</div>
</section>

<!-- 13 active intelligence -->
<section class="slide c1 r5">
  <div class="caps" style="left:18px;top:14px;font-size:13px">ACTIVE<br><b>INTELLIGENCE</b></div>
  <div class="body" style="left:18px;top:48px;width:148px;font-size:3.9px;text-align:justify">
    <p>Lorem ipsum dolor sit amet, consectetuer adipiscing elit, sed diam nonummy nibh euismod tincidunt ut laoreet dolore magna aliquam erat volutpat. Ut wisi enim ad minim veniam, quis nostrud exerci tation ullamcorper suscipit lobortis nisl ut aliquip ex ea commodo consequat. Duis autem vel eum iriure dolor in hendrerit in vulputate velit esse</p>
    <p style="margin-top:5px">Lorem ipsum dolor sit amet, consectetuer adipiscing elit, sed diam nonummy nibh euismod tincidunt ut laoreet dolore magna aliquam erat volutpat. Ut wisi enim ad minim veniam, quis nostrud exerci tation ullamcorper suscipit lobortis nisl ut aliquip ex ea commodo consequat. Duis autem vel eum iriure dolor in hendrerit in vulputate velit esse</p>
  </div>
  <svg class="abs" style="left:18px;top:136px" width="8" height="36" viewBox="0 0 8 36"><path d="M1 1 L6 4 L1 7 Z" fill="#0d5a6c"/><path d="M1 25 L6 28 L1 31 Z" fill="none" stroke="#0d5a6c" stroke-width=".6"/></svg>
  <div class="body" style="left:32px;top:134px;width:135px;font-size:3.8px;color:#7a8387">Lorem ipsum dolor sit amet, consectetuer adipiscing elit, sed diam nonummy nibh euismod tincidunt ut laoreet dolore magna</div>
  <div class="body" style="left:32px;top:158px;width:135px;font-size:3.8px;color:#7a8387">Lorem ipsum dolor sit amet, consectetuer adipiscing elit, sed diam nonummy nibh euismod tincidunt ut laoreet dolore magna</div>
  <div class="abs" style="left:259px;top:30px;width:88px;height:2px;background:var(--teal)"></div>
  <div class="abs" style="left:176px;top:92px;width:.8px;height:84px;background:var(--teal)"></div>
  <div class="photo" role="img" aria-label="Photo of a laptop on a desk in front of a window with a city skyline" style="left:181px;top:36px;width:186px;height:137px"></div>
  <div class="footer-brand">BRIGHT LANTERN</div><div class="footer-rule"></div><div class="footer-page">13</div>
</section>

<!-- 14 split layout -->
<section class="slide c2 r5">
  <div class="caps" style="left:20px;top:23px;font-size:11.4px">WHAT'S A DOMAIN?<br>IT'S THAT NAME UP<br><b>IN THE ADDRESS BAR.</b></div>
  <ul class="plain-list tick-list" style="left:20px;top:78px;font-size:8.4px">
    <li style="margin-bottom:7.5px">Fits your business or products</li><li style="margin-bottom:7.5px">Is easy to spell and remember</li><li style="margin-bottom:7.5px">Fits your business or products</li><li style="margin-bottom:7.5px">Is easy to spell and remember</li><li style="margin-bottom:7.5px">Fits your business or products</li><li style="margin-bottom:7.5px">Is easy to spell and remember</li>
  </ul>
  <div class="teal-panel" style="left:174px;top:0;width:163px;height:206px"></div>
  <div class="caps" style="left:181px;top:22px;font-size:13px;color:#fff">LOREM IPSUM<br><b>DOLOR SIT AMET</b></div>
  <div class="panel-text" style="left:181px;top:55px;width:148px">Lorem ipsum dolor sit amet, consectetuer adipiscing elit, sed diam nonummy nibh euismod tincidunt ut laoreet dolore magna aliquam erat volutpat. Ut wisi enim ad minim veniam, quis nostrud exerci tation ullamcorper suscipit lobortis nisl ut aliquip ex ea commodo consequat. Duis autem vel eum iriure dolor in hendrerit in vulputate velit esse</div>
  <div class="panel-text" style="left:181px;top:110px;width:148px">Lorem ipsum dolor sit amet, consectetuer adipiscing elit, sed diam nonummy nibh euismod tincidunt ut laoreet dolore magna aliquam erat volutpat. Ut wisi enim ad minim</div>
  <svg class="abs" style="left:181px;top:145px" width="8" height="30" viewBox="0 0 8 30"><path d="M1 1 L6 4 L1 7 Z" fill="#fff"/><path d="M1 22 L6 25 L1 28 Z" fill="none" stroke="#fff" stroke-width=".6"/></svg>
  <div class="panel-text" style="left:196px;top:144px;width:133px;font-size:3.9px">Lorem ipsum dolor sit amet, consectetuer adipiscing elit, sed diam nonummy nibh euismod tincidunt ut laoreet dolore magna</div>
  <div class="panel-text" style="left:196px;top:168px;width:133px;font-size:3.9px">Lorem ipsum dolor sit amet, consectetuer adipiscing elit, sed diam nonummy nibh euismod tincidunt ut laoreet dolore</div>
  <div class="footer-brand">BRIGHT LANTERN</div>
  <div class="footer-rule" style="right:193px"></div>
  <div class="abs" style="left:337px;right:17px;top:190px;height:.5px;background:var(--teal)"></div>
  <div class="footer-page">13</div>
</section>

<!-- 15 closing -->
<section class="slide c3 r5 cover">
  <div class="thanks">Thank you!</div>
</section>

</body>
</html>
```